Website design for Cambridge based systematic hedge fund

We have run previous craftmosaic competitions to design our company logo, business cards and the styling of our presentation deck (see attached files).
As the final step we are looking to get a website designed that is thematically consistent with these existing elements of our branding.
You can find some of our competitors websites below:
https://www.quelmarsh.example/
https://www.fenloor.example/
https://www.pyvart.example/
https://www.dulvet.example/
https://www.orbelmfunds.example/
https://www.valtrigo.example/
https://www.meskilfunds.example/home
We would like to have a website that works well on both mobile devices and desktops. Either just as one page that can be scrolled down, with links at the top that skips to certain sections, or a few separate pages that can be navigated by a top menu.
It should look professional, we are not after lots of animations or unnecessary transitions, and in particular the website must be smooth to navigate. We would like to avoid having peoples of people, we are happy to make use of elements from the presentation (for example the style of the cover slide, or the section slides with the faded bridge in the background), or 'financial' style images.
We would like to have the following sections for now. For some of these some example text has been provided, final text may change but it will be of similar length. For the other sections we are happy to just have template text for now. At the moment we are mainly interested to see styles/layouts as words can be added easily afterwards:
1) We will need a disclaimer pop up the first time someone visits the site (see for example the meskilfunds example).
2) Top page - company name, then in larger text "Bringing AI and Statistical Inference to Financial Markets", and somewhere in smaller text "Harlow Vectors is a quantitative asset manager with the singular focus of delivering algorithmic strategies that work"
3) "About us" section: will describe us as a company, details our approach, company values, and explains the company logo.
Example text:
"We deliver consistent alpha across liquid markets through the application of proprietary IP in Bayesian inference, machine learning and artificial intelligence. We are a multi-disciplinary team founded by experienced finance professionals from premier institutions, leading academics from the Thornbury Stellar Unit at Ashmere College and world-class software engineers.
Our logo portrays a sillhoute of the lattice walkway at Ashmere College. Our unique scientific approach allows us to bridge cutting-edge mathematical research and computing expertise with financial knowledge to bring algorithmns that work to liquid markets"
4) Hiring section, detailing our culture, what we are looking for.
Example text:
"We are always looking for exceptional talent to join our entrepreneurial team. We are looking for individuals who are creative thinkers, can demonstrate analytical rigour and are passionate about the intersection of science, finance and technology.
We prioritise having a company culture that promotes sharing ideas in a safe, collaborative research environment. We make sure that every member of the team has the oppertunity to explore their own ideas through weekly 'innovation time', and ensure that everyone gets the support they need to continue to grow as individuals within the company."
5) A section for news/press releases
6) Contact us area at the bottom with office location and email. We will need to list 3 addresses for our Cambridge, London and Singapore offices, along with a couple of contact emails or phone numbers
7) A client login button at the top that will take them to a different website (unrelated to this one).

```html
<!DOCTYPE html>
<html lang="en">
<head>
<meta charset="utf-8">
<title>Harlow Vectors — Quantitative Asset Management</title>
<link rel="stylesheet" href="https://fonts.googleapis.com/css2?family=Outfit:wght@300;400;500;600;700&family=Montserrat:wght@700&display=swap">
<style>
:root{
  --navy:#0b3f73;
  --navy-deep:#093663;
  --blue:#4a8fd9;
  --blue-soft:#bcd6f3;
  --wash:#eef4fb;
  --ink:#2f3540;
  --muted:#8a8f98;
  --white:#ffffff;
}
*{box-sizing:border-box;margin:0;padding:0}
html,body{width:1200px;height:3313px;overflow:hidden}
body{position:relative;background:var(--white);font-family:"Outfit",sans-serif;color:var(--ink)}
.abs{position:absolute}
a{color:inherit;text-decoration:none}

/* header */
.brand{left:178px;top:54px;width:170px;text-align:center;color:var(--navy);font-weight:600;font-size:21px;line-height:1;white-space:nowrap;display:flex;align-items:center;justify-content:center;gap:7px}
.brand-mark{width:10px;height:10px;background:var(--navy);border-radius:50%}
.call{left:904px;top:11px;display:flex;align-items:center;gap:10px;color:var(--navy)}
.call .lbl{border-left:1px solid var(--navy);padding-left:8px;font-size:8px;font-weight:600;line-height:1.2}
.call .lbl b{display:block;font-size:12px;font-weight:500}
.login{left:1084px;top:10px;width:108px;height:27px;border-radius:14px;background:var(--blue);color:var(--white);font-size:11px;display:flex;align-items:center;justify-content:center}
.nav{left:412px;top:46px;width:788px;height:37px;background:var(--navy);border-radius:18px 0 0 18px;display:flex;align-items:center;padding-left:42px;gap:42px;color:var(--white);font-size:13px;font-weight:500}

/* hero */
.hero-bg{left:0;top:0;width:1200px;height:780px;background:linear-gradient(180deg,#f8fbfe 0%,#f0f5fb 70%,#f5f8fd 100%)}
.hero-wave{left:0;top:640px;width:1200px;height:160px}
.hero-art{left:0;top:240px;width:560px;height:300px;border-radius:10px 45% 60% 30% / 20% 40% 70% 60%;background:radial-gradient(ellipse at 30% 40%,rgba(11,63,115,.55),rgba(74,143,217,.35) 55%,rgba(188,214,243,.15) 80%,transparent 100%);transform:rotate(12deg);transform-origin:0 0}
.hero-title{left:653px;top:262px;font-size:38px;line-height:49px;font-weight:500;color:var(--navy-deep)}
.hero-copy{left:653px;top:434px;width:350px;font-size:12px;line-height:20px;color:var(--ink)}

/* about */
.about-photo{left:0;top:819px;width:463px;height:422px;background:linear-gradient(135deg,#d5dbe3,#8c98a8 55%,#4f5c70);border-radius:0 62% 58% 0 / 0 48% 52% 0;box-shadow:5px 4px 0 var(--blue-soft)}
.section-title{font-size:36px;font-weight:700;color:var(--blue);letter-spacing:-.5px}
.about-title{left:576px;top:874px}
.about-copy{left:576px;top:940px;width:415px;font-size:11px;line-height:22px;color:var(--ink)}
.about-copy p+p{margin-top:19px;line-height:19px}
.about-fade{left:836px;top:1130px;width:364px;height:190px;background:linear-gradient(170deg,rgba(11,63,115,.06),rgba(11,63,115,.02));border-radius:40% 10% 60% 30%}

/* hiring */
.hiring-bg{left:0;top:1300px;width:1200px;height:900px;background:linear-gradient(180deg,#eef4fb,#f6f9fd 70%,#fff)}
.hiring-title{left:193px;top:1538px}
.hiring-copy{left:193px;top:1604px;width:350px;font-size:13px;line-height:22.5px}
.btn-pill{left:193px;top:1742px;width:108px;height:27px;border-radius:14px;background:var(--blue);color:var(--white);font-size:11px;display:flex;align-items:center;justify-content:center}
.hiring-art{left:655px;top:1470px;width:400px;height:400px;border-radius:48% 52% 40% 60% / 45% 40% 60% 55%;background:radial-gradient(ellipse at 50% 40%,#8db8e8,#c5daf3 60%,#dce8f7)}

/* blog */
.eyebrow{left:0;width:1200px;top:2204px;text-align:center;font-size:13px;letter-spacing:3px;font-weight:500;color:var(--blue)}
.blog-title{left:0;width:1200px;top:2228px;text-align:center;font-size:38px;font-weight:300;color:var(--ink)}
.blog-title b{font-weight:700}
.blog-intro{left:300px;width:600px;top:2296px;text-align:center;font-size:14px;line-height:28px;color:var(--muted)}
.card{top:2392px;width:321px;height:411px;background:var(--white);box-shadow:0 10px 30px rgba(11,63,115,.08)}
.card .thumb{position:absolute;left:9px;top:13px;width:303px;height:208px}
.card .date{position:absolute;left:18px;top:-8px;width:63px;height:63px;border-radius:50% 50% 50% 8%;background:var(--blue);border:3px solid var(--white);color:var(--white);text-align:center;font-size:26px;font-weight:600;line-height:28px;padding-top:5px}
.card .date small{display:block;font-size:11px;font-weight:400;line-height:10px}
.card h3{position:absolute;left:18px;top:244px;width:250px;font-family:"Montserrat",sans-serif;font-size:15px;line-height:25px;color:#1c2330}
.card p{position:absolute;left:18px;top:302px;width:290px;font-size:12px;line-height:22px;color:var(--muted)}
.card svg{position:absolute;left:18px;top:384px}
.view-all{left:511px;top:2852px;width:176px;height:41px;border:1.5px solid #a9adb4;border-radius:21px;font-size:12px;letter-spacing:1px;font-weight:500;color:#6b7079;display:flex;align-items:center;justify-content:center}

/* footer */
.footer{left:0;top:2970px;width:1200px;height:343px;background:var(--navy);color:var(--white)}
.footer .brand{left:178px;top:110px;color:var(--white)}
.footer .brand-mark{background:var(--white)}
.f-btn{left:188px;top:193px;width:142px;height:29px;border-radius:15px;background:var(--blue);font-size:11px;display:flex;align-items:center;justify-content:center}
.f-rule{top:58px;width:1px;height:180px;background:rgba(255,255,255,.15)}
.f-col h4{font-size:16px;font-weight:400;color:#6fa6e6;position:relative}
.f-col h4::before{content:"";position:absolute;left:0;top:-12px;width:28px;height:2px;background:#6fa6e6}
.f-col ul{list-style:none;font-size:11px;line-height:21.5px;margin-top:16px}
.f-item{display:flex;gap:10px;font-size:11px;line-height:17px;margin-top:10px}
.social{display:flex;gap:5px;margin-top:14px}
.social span{width:21px;height:21px;border-radius:50%;background:#4a8fd9}
.news-in{margin-top:14px;display:flex}
.news-in span{width:124px;height:27px;background:var(--white);color:#888;font-size:9px;padding:8px 10px}
.news-in i{width:24px;height:27px;background:var(--blue);display:flex;align-items:center;justify-content:center}
.f-bottom{left:0;top:280px;width:1200px;border-top:1px solid rgba(255,255,255,.15)}
.f-bottom span{position:absolute;top:26px;font-size:11px}
</style>
</head>
<body>

<div class="abs hero-bg"></div>
<svg class="abs hero-wave" viewBox="0 0 1200 160" preserveAspectRatio="none"><path d="M0 60C250 20 450 60 700 40S1050 0 1200 60V160H0z" fill="#fff"/></svg>
<div class="abs hero-art" role="img" aria-label="Brand lattice walkway graphic in navy and light blue"></div>

<header>
  <div class="abs brand"><span class="brand-mark"></span>Harlow Vectors</div>
  <div class="abs call">
    <svg width="22" height="22" viewBox="0 0 24 24" fill="none" stroke="#0b3f73" stroke-width="2"><path d="M5 3h4l2 5-3 2a11 11 0 0 0 6 6l2-3 5 2v4a2 2 0 0 1-2 2A17 17 0 0 1 3 5a2 2 0 0 1 2-2z"/></svg>
    <div class="lbl">CALL US NOW<b>140 2286 5173</b></div>
  </div>
  <a class="abs login" href="#">CLIENT LOGIN</a>
  <nav class="abs nav"><a href="#">HOME</a><a href="#">ABOUT US</a><a href="#">SERVICES</a><a href="#">HIRING</a><a href="#">NEWS</a><a href="#">CONTACT US</a></nav>
</header>

<h1 class="abs hero-title">Bringing AI and<br>Statistical Inference<br>to Financial Markets</h1>
<p class="abs hero-copy">Harlow Vectors is a quantitative asset manager with the singular focus of delivering algorithmic strategies that work</p>

<div class="abs about-fade" role="img" aria-label="Faint brand lattice decoration"></div>
<div class="abs about-photo" role="img" aria-label="Team collaborating at a whiteboard in an office"></div>
<h2 class="abs section-title about-title">ABOUT US</h2>
<div class="abs about-copy">
  <p>We deliver consistent alpha across liquid markets through the application of proprietary IP in Bayesian inference, machine learning and artificial intelligence. We are a multi-disciplinary team founded by experienced finance professionals from premier institutions, leading academics from the Thornbury Stellar Unit at Ashmere College and world-class software engineers.</p>
  <p>Our logo portrays a sillhoute of the lattice walkway at Ashmere College. Our unique scientific approach allows us to bridge cutting-edge mathematical research and computing expertise with financial knowledge to bring algorithmns that work to liquid markets</p>
</div>

<div class="abs hiring-bg"></div>
<svg class="abs" style="left:0;top:1290px" width="1200" height="130" viewBox="0 0 1200 130" preserveAspectRatio="none"><path d="M0 0H1200V70C1000 130 800 40 600 60S200 130 0 80z" fill="#fff"/></svg>
<h2 class="abs section-title hiring-title">WE ARE HIRING</h2>
<p class="abs hiring-copy">We are always looking for exceptional talent to join our entrepreneurial team. We are looking for individuals who are creative thinkers, can demonstrate analytical rigour and are passionate about the intersection of science, finance and technology.</p>
<a class="abs btn-pill" href="#">LEARN MORE</a>
<div class="abs hiring-art" role="img" aria-label="Illustration of hands typing on a laptop beside a plant and notepad"></div>
<svg class="abs" style="left:0;top:1850px" width="1200" height="200" viewBox="0 0 1200 200" fill="none" stroke="#bcd6f3" stroke-width="1.5"><path d="M0 5C150 90 300 190 600 200C850 205 1000 110 1200 140"/></svg>

<p class="abs eyebrow">RESOURCES</p>
<h2 class="abs blog-title">Blog <b>Posts</b></h2>
<p class="abs blog-intro">Lorem ipsum dolor sit amet, consectetur adipiscing elit. Ut in ipsum a augue tincidunt pulvinar. Donec feugiat ornare justo Morbi ornare dui at iaculis luctus.</p>
<svg class="abs" style="left:0;top:2500px" width="1200" height="200" viewBox="0 0 1200 200" fill="none" stroke="#3d86d6" stroke-width="1.5"><path d="M0 150C200 100 350 110 600 120C850 130 1050 110 1200 20"/></svg>

<article class="abs card" style="left:98px">
  <div class="thumb" role="img" aria-label="Phone showing a finance approval message" style="background:linear-gradient(135deg,#dfe9f5,#7fa6d3)"></div>
  <div class="date">18<small>FEB</small></div>
  <h3>Neque porro quisquam est qui dolorem ipsum quia dolor.</h3>
  <p>Lorem ipsum dolor sit amet, consectetur adipiscing elit. Pellentesque fermentum eros justo, aliquam lacinia justo.</p>
  <svg width="30" height="10" viewBox="0 0 30 10" fill="none" stroke="#4a8fd9"><path d="M0 5h29M24 1l5 4-5 4"/></svg>
</article>
<article class="abs card" style="left:438px">
  <div class="thumb" role="img" aria-label="Calculator and paperwork on a desk" style="background:linear-gradient(135deg,#e9ecf0,#8a95a3)"></div>
  <div class="date">18<small>FEB</small></div>
  <h3>Neque porro quisquam est qui dolorem ipsum quia dolor.</h3>
  <p>Lorem ipsum dolor sit amet, consectetur adipiscing elit. Pellentesque fermentum eros justo, aliquam lacinia justo.</p>
  <svg width="30" height="10" viewBox="0 0 30 10" fill="none" stroke="#4a8fd9"><path d="M0 5h29M24 1l5 4-5 4"/></svg>
</article>
<article class="abs card" style="left:778px">
  <div class="thumb" role="img" aria-label="Piggy bank wearing a face mask" style="background:linear-gradient(135deg,#f1e4e6,#a9c7c2)"></div>
  <div class="date">18<small>FEB</small></div>
  <h3>Neque porro quisquam est qui dolorem ipsum quia dolor.</h3>
  <p>Lorem ipsum dolor sit amet, consectetur adipiscing elit. Pellentesque fermentum eros justo, aliquam lacinia justo.</p>
  <svg width="30" height="10" viewBox="0 0 30 10" fill="none" stroke="#4a8fd9"><path d="M0 5h29M24 1l5 4-5 4"/></svg>
</article>
<a class="abs view-all" href="#">VIEW ALL POSTS</a>

<footer class="abs footer">
  <div class="abs brand"><span class="brand-mark"></span>Harlow Vectors</div>
  <a class="abs f-btn" href="#">CONTACT US NOW</a>
  <div class="abs f-rule" style="left:374px"></div>
  <div class="abs f-rule" style="left:543px"></div>
  <div class="abs f-rule" style="left:797px"></div>

  <div class="abs f-col" style="left:429px;top:84px">
    <h4>Site Links</h4>
    <ul><li>Home</li><li>About Us</li><li>Services</li><li>News</li><li>Contact Us</li></ul>
  </div>
  <div class="abs f-col" style="left:586px;top:84px;width:205px">
    <h4>Contact Us</h4>
    <div class="f-item" style="margin-top:18px"><svg width="14" height="14" viewBox="0 0 24 24" fill="none" stroke="#6fa6e6" stroke-width="2"><path d="M5 3h4l2 5-3 2a11 11 0 0 0 6 6l2-3 5 2v4a2 2 0 0 1-2 2A17 17 0 0 1 3 5a2 2 0 0 1 2-2z"/></svg>Phone: 140 228 65173</div>
    <div class="f-item"><svg width="14" height="14" viewBox="0 0 24 24" fill="none" stroke="#6fa6e6" stroke-width="2"><path d="M12 22s7-7 7-12a7 7 0 0 0-14 0c0 5 7 12 7 12z"/><circle cx="12" cy="10" r="2.5"/></svg><span>Address: 48 Larkspur Row in<br>Elmvale at 9th Lane, 14th<br>Brindle City, Bc</span></div>
    <div class="f-item"><svg width="14" height="14" viewBox="0 0 24 24" fill="none" stroke="#6fa6e6" stroke-width="2"><rect x="3" y="5" width="18" height="14" rx="2"/><path d="M3 7l9 6 9-6"/></svg>Email: mail@harlowvectors.example</div>
  </div>
  <div class="abs f-col" style="left:853px;top:84px">
    <h4>Get Connected</h4>
    <div class="social"><span></span><span></span><span></span></div>
    <h4 style="margin-top:50px">Newsletter</h4>
    <div class="news-in"><span>Email...</span><i><svg width="12" height="12" viewBox="0 0 24 24" fill="#fff"><path d="M2 11L22 2l-9 20-2-8z"/></svg></i></div>
  </div>

  <div class="abs f-bottom">
    <span style="left:193px">@2021 Harlow Vectors &nbsp;|&nbsp; All Rights Reserved.</span>
    <span style="left:814px">Terms &amp; Conditions &nbsp;|&nbsp; Privacy Policy</span>
  </div>
</footer>

</body>
</html>
```